Values and Organizational Purpose Signage

We recently solidified our company values, organizatioanal purpose and strategic vision. I'd like to develop some tasteful (not overly corporate) signage of these values to display in our office.

I've attached the hand-written values and purpose that my core team members then initialed acknowleding they align along with the signage at the front of our office to provide some perspective on our brand identity.

Industry/Entity Type

It Company

Font styles to use
Sans Serif

Requirements
Must have
• I'd like to see the values and org purpose depicted as one sign and as separate signs (i.e., values on one sign and org purpose on another). I need it to reflect our brand identity which I've uploaded

```html
<!DOCTYPE html>
<html lang="en">
<head>
<meta charset="utf-8">
<title>Organizational Purpose and Core Values Signage</title>
<link rel="stylesheet" href="https://fonts.googleapis.com/css2?family=Jost:wght@400;500;700;800&display=swap">
<style>
  :root {
    --wall: #4f8d0a;
    --panel: #ffffff;
    --ink: #003236;
    --lime: #9fd232;
  }
  * { margin: 0; padding: 0; box-sizing: border-box; }
  html, body { width: 1010px; height: 1200px; overflow: hidden; }
  body {
    background: var(--wall);
    font-family: "Jost", sans-serif;
    color: var(--ink);
    position: relative;
  }
  .sign {
    position: absolute;
    left: 51px;
    width: 908px;
    background: var(--panel);
    overflow: hidden;
  }
  .sign--purpose { top: 55px; height: 316px; }
  .sign--values { top: 499px; height: 621px; }
  .standoff {
    position: absolute;
    width: 12px; height: 12px;
    border-radius: 50%;
    background: var(--ink);
  }
  .standoff--tl { left: 6px; top: 10px; }
  .standoff--tr { right: 6px; top: 10px; }
  .standoff--bl { left: 6px; bottom: 10px; }
  .standoff--br { right: 6px; bottom: 10px; }
  .sign-title {
    position: absolute;
    left: 73px;
    font-weight: 800;
    letter-spacing: 0;
    line-height: 1;
    white-space: nowrap;
  }
  .sign--purpose .sign-title { top: 66px; font-size: 52px; }
  .sign--values .sign-title { top: 60px; font-size: 64px; left: 70px; }
  .rule {
    position: absolute;
    left: 73px;
    width: 762px;
    height: 7px;
    background: var(--lime);
  }
  .sign--purpose .rule { top: 131px; }
  .purpose-statement {
    position: absolute;
    left: 73px;
    top: 155px;
    font-size: 45px;
    font-weight: 400;
    line-height: 52px;
    white-space: nowrap;
  }
  .value-label {
    position: absolute;
    left: 72px;
    font-size: 31px;
    font-weight: 800;
    line-height: 39px;
    letter-spacing: 0.3px;
  }
  .value-text {
    position: absolute;
    left: 390px;
    font-size: 26px;
    font-weight: 400;
    line-height: 31px;
    white-space: nowrap;
  }
  .sign--values .rule { left: 70px; width: 761px; }
</style>
</head>
<body>
  <section class="sign sign--purpose">
    <span class="standoff standoff--tl"></span>
    <span class="standoff standoff--tr"></span>
    <span class="standoff standoff--bl"></span>
    <span class="standoff standoff--br"></span>
    <h1 class="sign-title">ORGANIZATIONAL PURPOSE</h1>
    <div class="rule"></div>
    <p class="purpose-statement">We deliver simple and digestible<br>solutions to complex matters</p>
  </section>

  <section class="sign sign--values">
    <span class="standoff standoff--tl"></span>
    <span class="standoff standoff--tr"></span>
    <span class="standoff standoff--bl"></span>
    <span class="standoff standoff--br"></span>
    <h2 class="sign-title">CORE VALUES DEFINED</h2>

    <h3 class="value-label" style="top:170px">RESPECT</h3>
    <p class="value-text" style="top:147px">We are transparent and receptive to the<br>thoughts, opinion and feelings of others</p>
    <div class="rule" style="top:220px"></div>

    <h3 class="value-label" style="top:272px">INTEGRITY</h3>
    <p class="value-text" style="top:268px">We uphold our promises</p>
    <div class="rule" style="top:325px"></div>

    <h3 class="value-label" style="top:378px">EXCELLENCE</h3>
    <p class="value-text" style="top:353px">We continuously strive to be the best in<br>all endeavors</p>
    <div class="rule" style="top:431px"></div>

    <h3 class="value-label" style="top:467px">OPEN<br>MINDEDNESS</h3>
    <p class="value-text" style="top:465px">We encourage creative and innovative<br>expressions</p>
  </section>
</body>
</html>
```